Verdel Harvest Co - Business Card Design Project

We need business cards for our business. We grow roots and fruits in Central and South America, we import and distribute in FL, USA. We do fresh and frozen products.

Target Market(s)

Small and big supermarkets, wholesalers, traders, distributors, etc

Industry/Entity Type

Business

```html
<!DOCTYPE html>
<html lang="en">
<head>
<meta charset="utf-8">
<title>Verdel Harvest Co — Business Card</title>
<link href="https://fonts.googleapis.com/css2?family=Open+Sans:wght@400;600;700&display=swap" rel="stylesheet">
<style>
  :root {
    --olive: #4f5f31;
    --text-grey: #6b6b6b;
    --card: #ffffff;
    --bg-start: #b5c8d5;
    --bg-end: #eff2f5;
  }
  html, body {
    margin: 0;
    padding: 0;
    width: 1200px;
    height: 1000px;
    overflow: hidden;
  }
  .canvas {
    position: relative;
    width: 1200px;
    height: 1000px;
    background: linear-gradient(135deg, var(--bg-start) 0%, #d3dde5 50%, var(--bg-end) 100%);
    font-family: "Open Sans", Arial, sans-serif;
  }
  .card {
    position: absolute;
    left: 309px;
    width: 548px;
    height: 313px;
    background: var(--card);
    overflow: hidden;
  }
  .card--front { top: 124px; }
  .card--back { top: 587px; }

  .side-band {
    position: absolute;
    left: 0;
    top: 0;
    width: 56px;
    height: 100%;
    background: var(--olive);
  }
  .band-dots {
    position: absolute;
    left: 25px;
    top: 220px;
    display: flex;
    flex-direction: column;
    gap: 15px;
  }
  .band-dots span {
    width: 9px;
    height: 9px;
    border-radius: 50%;
    background: var(--card);
  }

  .wordmark {
    display: flex;
    align-items: center;
    gap: 8px;
    color: var(--olive);
    font-weight: 600;
    letter-spacing: 0.02em;
    white-space: nowrap;
  }
  .wordmark__dot {
    border-radius: 50%;
    background: var(--olive);
    flex: none;
  }
  .wordmark--small {
    position: absolute;
    left: 81px;
    top: 46px;
    font-size: 20px;
  }
  .wordmark--small .wordmark__dot { width: 12px; height: 12px; }

  .holder-name {
    position: absolute;
    right: 14px;
    top: 141px;
    margin: 0;
    font-size: 22px;
    font-weight: 700;
    color: var(--olive);
    letter-spacing: 0.01em;
  }
  .divider {
    position: absolute;
    left: 81px;
    right: 0;
    top: 185px;
    height: 2px;
    background: var(--olive);
  }
  .contact {
    position: absolute;
    left: 81px;
    top: 211px;
    margin: 0;
    padding: 0;
    list-style: none;
    color: var(--text-grey);
  }
  .contact__phone { font-size: 18px; line-height: 24px; }
  .contact__line { font-size: 14px; line-height: 24px; }

  .wordmark--large {
    position: absolute;
    left: 0;
    right: 0;
    top: 130px;
    justify-content: center;
    font-size: 36px;
    gap: 14px;
  }
  .wordmark--large .wordmark__dot { width: 20px; height: 20px; }
</style>
</head>
<body>
<main class="canvas">
  <section class="card card--front" aria-label="Business card front">
    <div class="side-band">
      <div class="band-dots"><span></span><span></span><span></span></div>
    </div>
    <div class="wordmark wordmark--small"><span class="wordmark__dot"></span>VERDEL HARVEST CO</div>
    <h1 class="holder-name">MARCO SALINAS</h1>
    <div class="divider"></div>
    <ul class="contact">
      <li class="contact__phone">0405551872</li>
      <li class="contact__line">support@verdelharvest.com</li>
      <li class="contact__line">www.verdelharvest.com</li>
    </ul>
  </section>

  <section class="card card--back" aria-label="Business card back">
    <div class="wordmark wordmark--large"><span class="wordmark__dot"></span>VERDEL HARVEST CO</div>
  </section>
</main>
</body>
</html>
```